Tahiti B&B Website (Coded)

Re design and optimization of a website for pension Vai Roa, a b&b in Tahiti, French Polynesia.

We have a website already : www.pensionvairoa.example

The general idea is to create a new site that is colorful, young and with an exotic, tropical feel since we are on a beautiful island.

The website will be in three languages, all the text is already available on our website, nothing changes.

All pages must have the name of the website (pension vai roa b&b) our address, mail and phone number
It would be nice to have a link to our mail from every page

Sections have to be easy to update : text and pics

The sections needed are :

- Home page (accueil)

- Prices (tarifs)

- Bookings (reservations) = link to our mailbox : pensionvairoa@courriel.example )

- Pictures : in three separate categories that will pop up on this page : 1/ pics of the b&b 2/ pics of the surroundings 3/ customer's pics (we'll give new pics, not the current ones)

- Map of Tahiti : we'd like one map that we'll give you and also a Google map with our location, date and local time would be great

- Links (liens)

We let you see what would look best for the top banner and the switches, matching the logo and the pictures, make it nice and tropical !!
We have a few layouts that we did, maybe you will have a better idea of what we want by looking at them, if you can use them and have a good overall feel

We'd like to remind you guys that Tahiti is a dream destination, so you have to come up with something that the visitors will go : wow !!

We cater for backpackers to mid range accommodations and families, it all about a relaxed friendly atmosphere here !

NOTE THAT WE DON'T KNOW MUCH ABOUT PROGRAMMING AND CODING SO IT AS TO BE READY TO GO ON-LINE, ALL YOUR HELP IS APPRECIATED !!!
Also in Tahiti, the
INTERNET is quite low bandwidth so optimization is a must !

P.S : Live demo of the homepage is welcome ;)

We are available to all you for extra infos, good luck

regards,

remy & Pension Vai Roa

Target Market(s)

Families and couples : individual rooms

Backpackers : Dormitories

people looking for an authentic stay in a familial environment

Customers of all ages and all nationalities

Industry/Entity Type

Internet

Requirements
Must have
• You must insist on the main page about :
the easy beach access
the breakfast included (with French baguette !)
Airport pick up 24/7
Many activities departing from our place : scuba diving, canyoning, 4x4 tour, rental cars, surf school, para-glide....

Please find a great way to highlight these !

```html
<!DOCTYPE html>
<html lang="en">
<head>
<meta charset="utf-8">
<title>Pension Vai Roa – Reservation Request</title>
<link rel="stylesheet" href="https://fonts.googleapis.com/css2?family=Arimo:wght@400;700&family=Tinos:wght@400;700&display=swap">
<style>
:root{
  --yellow:#ffff10;
  --nav-red:#e0301e;
  --green:#4e8a1e;
  --green-btn:#7cbd2a;
  --text:#333;
  --label:#222;
  --field-border:#b9b9b9;
  --link:#1f5f9e;
  --panel:rgba(255,255,255,.93);
  --page:rgba(255,255,255,.72);
}
*{box-sizing:border-box;margin:0;padding:0}
html,body{width:1200px;height:1059px;overflow:hidden}
body{position:relative;font-family:Arimo,Arial,sans-serif;color:var(--text);background:#fff}
.backdrop{position:absolute;inset:0;
  background:linear-gradient(180deg,#6fa9d6 0%,#a9d3ea 38%,#5fb4c8 62%,#4f9e7a 78%,#d9cfae 100%)}
.page{position:absolute;left:167px;top:44px;width:866px;height:979px}
.masthead{position:absolute;left:0;top:0;width:866px;height:149px;background:var(--yellow)}
.phone{position:absolute;left:497px;top:48px;font-weight:700;font-size:26px;color:#111}
.phone small{position:absolute;right:-10px;top:-14px;font-size:11px;font-weight:700}
.brand-name{position:absolute;left:690px;top:53px;font-size:19px;font-weight:700;color:var(--nav-red)}
.mainnav{position:absolute;left:10px;top:130px;display:flex;font-size:11px;font-weight:700;color:var(--nav-red)}
.mainnav a{color:inherit;text-decoration:none;padding:0 12px 0 0;margin-right:12px;border-right:1px solid #c9c400}
.mainnav a:last-child{border:0}
.content{position:absolute;left:0;top:149px;width:866px;height:762px;background:var(--page)}
.form-panel{position:absolute;left:57px;top:47px;width:468px;height:690px;background:var(--panel);border-radius:10px}
.form-title{position:absolute;left:18px;top:44px;font-size:22px;font-weight:400;color:var(--green);letter-spacing:.3px}
.f{position:absolute;font-size:11px;color:var(--label);white-space:nowrap}
.f b{font-weight:700}
.in{position:absolute;height:20px;border:1px solid var(--field-border);background:#fff}
.sel{position:absolute;height:16px;border:1px solid var(--field-border);background:#fff;font-size:10px;padding:1px 16px 1px 3px;white-space:nowrap}
.sel::after{content:"";position:absolute;right:0;top:0;width:13px;height:14px;border-left:1px solid var(--field-border);background:#eee}
.radio{position:absolute;width:11px;height:11px;border:1px solid #999;border-radius:50%;background:#fff}
.check{position:absolute;width:11px;height:11px;border:1px solid #999;background:#fff}
.submit{position:absolute;left:18px;top:616px;width:90px;height:30px;border-radius:15px;background:var(--green-btn);color:#fff;font-size:11px;font-weight:700;display:flex;align-items:center;justify-content:center}
.sidebar{position:absolute;left:603px;top:0;width:240px}
.lang{position:absolute;left:0;top:28px;width:142px;height:22px;border:1px solid #bbb;background:#fff;font-size:11px;padding:4px 0 0 24px}
.lang::before{content:"";position:absolute;left:6px;top:5px;width:12px;height:11px;background:#3a7ac8}
.side-title{position:absolute;left:0;top:70px;font-size:25px;font-weight:400;color:var(--green);white-space:nowrap}
.address{position:absolute;left:10px;top:106px;width:232px;font-family:Tinos,"Times New Roman",serif;font-size:12px;line-height:16px;color:#111}
.address strong{display:block;font-size:18px;line-height:26px;padding-left:36px}
.photo{position:absolute;left:2px;top:218px;width:240px;height:320px;background:linear-gradient(160deg,#5e8d3a 0%,#3d6b28 45%,#c24a3c 65%,#7a8f5a 100%)}
.contact{position:absolute;left:2px;top:552px;font-size:11px;font-weight:700;color:#333;white-space:nowrap}
.contact a{font-weight:400;color:var(--link);text-decoration:none}
.footer{position:absolute;left:0;top:911px;width:866px;height:68px;background:var(--yellow)}
.social{position:absolute;left:19px;top:21px;display:flex;gap:8px}
.social span{width:26px;height:26px;border-radius:5px}
.copyright{position:absolute;left:0;width:866px;top:28px;text-align:center;font-size:11px;color:#333}
.footnav{position:absolute;right:22px;top:28px;display:flex;gap:18px;font-size:11px}
.footnav a{color:#333;text-decoration:underline}
</style>
</head>
<body>
<div class="backdrop" role="img" aria-label="Tropical beach with palm trees, turquoise lagoon and island mountains"></div>

<div class="page">
  <header class="masthead">
    <div class="phone"><small>tahiti</small>Tel: 40 12 34</div>
    <div class="brand-name">Pension Vai Roa</div>
    <nav class="mainnav">
      <a>HOME</a><a>PRICES</a><a>BOOKING</a><a>GALLERY</a><a>MAP OF TAHITI</a><a>LINKS</a>
    </nav>
  </header>

  <main class="content">
    <section class="form-panel">
      <h1 class="form-title">RESERVATION REQUEST FORM</h1>

      <span class="f" style="left:18px;top:132px"><b>Name:</b></span>
      <span class="in" style="left:64px;top:126px;width:272px"></span>
      <span class="f" style="left:18px;top:170px"><b>Email:</b></span>
      <span class="in" style="left:66px;top:164px;width:270px"></span>

      <span class="f" style="left:18px;top:197px"><b>Arrival Date:</b></span>
      <span class="f" style="left:18px;top:216px">Month</span>
      <span class="sel" style="left:50px;top:214px;width:78px">- MONTH -</span>
      <span class="f" style="left:132px;top:216px">Day</span>
      <span class="sel" style="left:154px;top:214px;width:62px">- DAY -</span>
      <span class="f" style="left:220px;top:216px">Year</span>
      <span class="sel" style="left:246px;top:214px;width:68px">- YEAR -</span>

      <span class="f" style="left:18px;top:236px"><b>Departure Date:</b></span>
      <span class="f" style="left:18px;top:255px">Month</span>
      <span class="sel" style="left:50px;top:253px;width:78px">- MONTH -</span>
      <span class="f" style="left:132px;top:255px">Day</span>
      <span class="sel" style="left:154px;top:253px;width:62px">- DAY -</span>
      <span class="f" style="left:220px;top:255px">Year</span>
      <span class="sel" style="left:246px;top:253px;width:68px">- YEAR -</span>

      <span class="f" style="left:18px;top:308px"><b>Number of Guests:</b></span>
      <span class="in" style="left:132px;top:302px;width:120px"></span>
      <span class="f" style="left:18px;top:328px"><b>Do you need to be picked up at the airport?</b></span>
      <span class="radio" style="left:18px;top:356px"></span>
      <span class="f" style="left:36px;top:355px">Yes</span>
      <span class="radio" style="left:18px;top:376px"></span>
      <span class="f" style="left:36px;top:375px">No</span>

      <span class="f" style="left:18px;top:408px"><b>Arrival Time:</b></span>
      <span class="in" style="left:98px;top:402px;width:120px;height:18px"></span>
      <span class="f" style="left:18px;top:426px"><b>Flight Information :</b></span>
      <span class="in" style="left:138px;top:420px;width:120px;height:18px"></span>

      <span class="f" style="left:18px;top:506px"><b>Message:</b></span>
      <span class="in" style="left:76px;top:460px;width:272px;height:98px"></span>

      <span class="f" style="left:18px;top:574px">Send a copy to yourself?</span>
      <span class="check" style="left:146px;top:574px"></span>
      <span class="f" style="left:18px;top:594px"><span style="color:var(--link)">SumCheck</span> security question: 4 + 0 =</span>
      <span class="in" style="left:214px;top:590px;width:26px;height:18px"></span>

      <span class="submit">SUBMIT</span>
    </section>

    <aside class="sidebar">
      <div class="lang">Select Language &nbsp;▼</div>
      <h2 class="side-title">OUR ADDRESS</h2>
      <div class="address">
        <strong>Pension Vai Roa</strong>
        BP 40021 Hauroa 98799<br>
        Vai Tapu, Tahiti, French Polynesia.<br>
        Telephone: 40 12 34 77 21 09
      </div>
      <div class="photo" role="img" aria-label="Carved statue standing in a lush tropical garden"></div>
      <p class="contact">Contact Us: <a>pensionvairoa@courriel.example</a></p>
    </aside>
  </main>

  <footer class="footer">
    <div class="social">
      <span style="background:#f08a1c"></span>
      <span style="background:#3b6cb4"></span>
      <span style="background:#35a9e1"></span>
    </div>
    <p class="copyright">Copyright © 2011. All Rights Reserved.</p>
    <nav class="footnav"><a>About Us</a><a>Contact Us</a><a>Terms Of Service</a></nav>
  </footer>
</div>
</body>
</html>
```